Book Cover for Adult Coloring Book

I'd like a unique book cover design for a coloring book we are making for adults. The book cover is for an 8.5"x11" book. I need both the front and back cover created. We will want to include some text about the book on the back cover so there should be room for that. It will be less than 100 words.

1) The title is:

Grown-Up Doodle Pages: Cheeky Phrases To Leave Every Jaw Hanging Open

2) A swear word may appear on the cover, however it should similar to some of the examples included.

3) I'd prefer the background be in black or white so that the picture and color "pop" off the page more.

I've included 4 example covers that I really like. Something similar to these is preferred.

Reason: I've had a designer ask if we could extend the deadline. I'd like to get as many options as possible since this is a guaranteed project. Please extend it to Friday, February 19th, 2016. I may choose someone before then, but I'd like to see as many as possible before I do. Thank you, Marcus

Target Market(s)

Adults 25-65

Industry/Entity Type

Publishing Company

Font styles to use
Sans Serif
Decorative
Script

Requirements
Must have
• Unique design and be colorful. It's okay to have a swear word but it should be subtle and similar in design to some of the examples I provided.
Nice to have
• Black or white background that will allow the image/text to "pop" on the page.
Should not have
• No slurs, racial or homophobic words.

```html
<!DOCTYPE html>
<html lang="en">
<head>
<meta charset="utf-8">
<title>Grown-Up Doodle Pages: Cheeky Phrases To Leave Every Jaw Hanging Open</title>
<link href="https://fonts.googleapis.com/css2?family=Bowlby+One&family=Great+Vibes&display=swap" rel="stylesheet">
<style>
  :root {
    --bg: #000000;
    --script: #c8ff2e;
    --script-deep: #e6f03a;
    --block-red: #d8352a;
    --block-blue: #35b8e8;
    --block-edge: #f2d56b;
    --rainbow-red: #ff2a2a;
    --rainbow-orange: #ff8a00;
    --rainbow-yellow: #ffe600;
    --rainbow-green: #22e06a;
    --rainbow-cyan: #00d8ff;
    --rainbow-blue: #2a5cff;
    --rainbow-violet: #c02aff;
    --rainbow-pink: #ff2aa8;
  }
  html, body {
    margin: 0;
    padding: 0;
    width: 927px;
    height: 1200px;
    overflow: hidden;
    background: var(--bg);
  }
  .cover {
    position: relative;
    width: 927px;
    height: 1200px;
    background: var(--bg);
    overflow: hidden;
  }
  .ornament-frame {
    position: absolute;
    inset: 0;
    width: 927px;
    height: 1200px;
  }
  .title {
    position: absolute;
    left: 212px;
    width: 503px;
    margin: 0;
    text-align: center;
    font-weight: 400;
  }
  .title-script {
    font-family: "Great Vibes", cursive;
    color: var(--script);
    background: linear-gradient(180deg, var(--script-deep), var(--script));
    -webkit-background-clip: text;
    background-clip: text;
    -webkit-text-fill-color: transparent;
    white-space: nowrap;
  }
  .series {
    top: 362px;
    font-size: 52px;
    line-height: 1;
  }
  .headline {
    font-family: "Bowlby One", sans-serif;
    font-size: 92px;
    line-height: 0.92;
    letter-spacing: 1px;
    color: var(--block-blue);
    background: linear-gradient(90deg, var(--block-blue) 0%, var(--block-red) 30%, var(--block-blue) 55%, var(--block-red) 80%, var(--block-blue) 100%);
    -webkit-background-clip: text;
    background-clip: text;
    -webkit-text-fill-color: transparent;
    -webkit-text-stroke: 2px var(--block-edge);
  }
  .headline-top { top: 478px; }
  .headline-bottom { top: 566px; }
  .tagline {
    font-size: 56px;
    line-height: 1;
  }
  .tagline-top { top: 730px; }
  .tagline-bottom { top: 808px; }
</style>
</head>
<body>
  <main class="cover">
    <svg class="ornament-frame" viewBox="0 0 927 1200" role="img" aria-label="Rainbow swirl and butterfly ornamental frame surrounding the title">
      <defs>
        <linearGradient id="frame-rainbow" x1="0" y1="0" x2="1" y2="1">
          <stop offset="0" stop-color="var(--rainbow-green)"/>
          <stop offset="0.18" stop-color="var(--rainbow-cyan)"/>
          <stop offset="0.32" stop-color="var(--rainbow-violet)"/>
          <stop offset="0.46" stop-color="var(--rainbow-red)"/>
          <stop offset="0.6" stop-color="var(--rainbow-yellow)"/>
          <stop offset="0.74" stop-color="var(--rainbow-green)"/>
          <stop offset="0.88" stop-color="var(--rainbow-blue)"/>
          <stop offset="1" stop-color="var(--rainbow-pink)"/>
        </linearGradient>
      </defs>
      <path fill="url(#frame-rainbow)" fill-opacity="0.55" fill-rule="evenodd"
        d="M140 20 H900 Q920 20 920 40 V1110 Q920 1160 870 1160 H120 Q20 1160 20 1060 V120 Q20 20 140 20 Z
           M232 170 H700 Q718 170 718 188 V880 Q718 900 700 900 H232 Q214 900 214 880 V188 Q214 170 232 170 Z"/>
    </svg>

    <h1 class="title title-script series">Grown-Up Doodle Pages</h1>
    <p class="title headline headline-top">CHEEKY</p>
    <p class="title headline headline-bottom">PHRASES</p>
    <p class="title title-script tagline tagline-top">To Leave Every Jaw</p>
    <p class="title title-script tagline tagline-bottom">Hanging Open</p>
  </main>
</body>
</html>
```